BW Business Card

Used Car Sales
We are trying to recreate the image of our license plate on business cards,
it is a red background with a white oval that is open on the ends
I attempted to upload the image but it was a dismal failure when the products arrived
the lettering was too small and the edges were white
I think maybe the red needs some texture in it, still red but something that doesn't look so flat
and maybe a beveled edge around the white (not sure)

Target Market(s)

Adults 25-65 that drive

Industry/Entity Type

Business

Contact Information for Business Card

Darlene Whitcombe, Sales Manager, BRIGHTWAY AUTO MART, INC., 462 Fernhill Road, Pulaski, TN 38591,
931 587-2064 (office), 931 587-6259 (fax) - We Finance everyone with approved credit
BrightwayAutoMart.Com

On Back: Financing Available - We Finance everyone with approved credit
Easy Payments: Monthly, Semi-Monthly or Weekly
Ask about our Layaway plan
Open Mon-Sat
8:30 AM - 5 PM

Requirements
Must have
• We want to match the license plate (minus holes for screws)

```html
<!DOCTYPE html>
<html lang="en">
<head>
<meta charset="utf-8">
<title>Brightway Auto Mart – Business Card</title>
<link rel="stylesheet" href="https://fonts.googleapis.com/css2?family=Almendra:ital,wght@1,700&family=Caudex&family=Marcellus&display=swap">
<style>
  :root {
    --page: #f1ecec;
    --red-deep: #6e0f0c;
    --red: #9a1c14;
    --red-light: #b52a1d;
    --ink-red: #8e1a12;
    --ink: #111111;
    --oval: #ffffff;
    --bevel: #c9c9c9;
    --bevel-dark: #9d9d9d;
    --white-text: #f6f1ee;
  }
  * { margin: 0; padding: 0; box-sizing: border-box; }
  html, body { width: 1200px; height: 899px; overflow: hidden; background: var(--page); }
  .canvas { position: relative; width: 1200px; height: 899px; }

  .card { position: absolute; overflow: hidden; box-shadow: 0 6px 14px rgba(0,0,0,.25); }
  .card--front { left: 50px; top: 30px; width: 700px; height: 410px; }
  .card--back { left: 430px; top: 460px; width: 730px; height: 415px; }
  .card__plate { position: absolute; inset: 0; width: 100%; height: 100%; }

  .line { position: absolute; left: 0; right: 0; text-align: center; white-space: nowrap; }
  .serif { font-family: "Marcellus", "Caudex", serif; }
  .body { font-family: "Caudex", serif; }
  .script { font-family: "Almendra", serif; font-style: italic; font-weight: 700; }

  .contact-name { top: 62px; font-size: 38px; color: var(--ink-red); letter-spacing: 1px; }
  .contact-title { top: 112px; font-size: 23px; color: var(--ink-red); }
  .company { top: 146px; font-size: 36px; color: var(--ink); letter-spacing: 2px; }
  .address { top: 200px; font-size: 23px; color: var(--ink-red); }
  .phones { top: 236px; font-size: 18px; color: var(--ink-red); letter-spacing: .5px; }
  .tagline { top: 276px; font-size: 21px; color: var(--ink-red); letter-spacing: 1px; }
  .website { font-family: "Caudex", serif; font-size: 23px; color: var(--white-text); letter-spacing: 7px; }
  .card--front .website { top: 358px; }

  .finance-title { top: 28px; font-size: 38px; color: var(--ink-red); letter-spacing: 1px; }
  .finance-line { font-size: 21px; color: var(--ink); }
  .finance-line--1 { top: 80px; }
  .finance-line--2 { top: 108px; }
  .layaway { top: 140px; font-size: 36px; color: var(--ink); }
  .hours-days { top: 196px; font-size: 22px; color: var(--ink-red); }
  .hours-time { top: 224px; font-size: 33px; color: var(--ink-red); letter-spacing: 2px; }
  .social { top: 292px; font-size: 15px; color: var(--ink-red); letter-spacing: .5px; }
  .card--back .website { top: 350px; }
</style>
</head>
<body>
<main class="canvas">

  <section class="card card--front" aria-label="Business card front">
    <svg class="card__plate" viewBox="0 0 700 410" preserveAspectRatio="none" aria-hidden="true">
      <defs>
        <linearGradient id="plateRedFront" x1="0" y1="0" x2="1" y2="1">
          <stop offset="0" stop-color="var(--red-light)"/>
          <stop offset=".5" stop-color="var(--red)"/>
          <stop offset="1" stop-color="var(--red-deep)"/>
        </linearGradient>
        <linearGradient id="bevelFront" x1="0" y1="0" x2="0" y2="1">
          <stop offset="0" stop-color="var(--bevel)"/>
          <stop offset="1" stop-color="var(--bevel-dark)"/>
        </linearGradient>
      </defs>
      <rect width="700" height="410" fill="url(#plateRedFront)"/>
      <ellipse cx="350" cy="188" rx="432" ry="176" fill="url(#bevelFront)"/>
      <ellipse cx="350" cy="186" rx="420" ry="168" fill="var(--oval)"/>
    </svg>
    <p class="line serif contact-name">Darlene Whitcombe</p>
    <p class="line serif contact-title">Sales Manager</p>
    <p class="line serif company">BRIGHTWAY AUTO MART, INC</p>
    <p class="line serif address">462 Fernhill Road, Pulaski, TN 38591</p>
    <p class="line serif phones">931 587-2064 (office), 931 587-6259 (fax)</p>
    <p class="line script tagline">We Finance everyone with approved credit</p>
    <p class="line website">BrightwayAutoMart.Com</p>
  </section>

  <section class="card card--back" aria-label="Business card back">
    <svg class="card__plate" viewBox="0 0 730 415" preserveAspectRatio="none" aria-hidden="true">
      <defs>
        <linearGradient id="plateRedBack" x1="0" y1="0" x2="1" y2="1">
          <stop offset="0" stop-color="var(--red-light)"/>
          <stop offset=".5" stop-color="var(--red)"/>
          <stop offset="1" stop-color="var(--red-deep)"/>
        </linearGradient>
        <linearGradient id="bevelBack" x1="0" y1="0" x2="0" y2="1">
          <stop offset="0" stop-color="var(--bevel)"/>
          <stop offset="1" stop-color="var(--bevel-dark)"/>
        </linearGradient>
      </defs>
      <rect width="730" height="415" fill="url(#plateRedBack)"/>
      <ellipse cx="365" cy="182" rx="450" ry="176" fill="url(#bevelBack)"/>
      <ellipse cx="365" cy="180" rx="438" ry="168" fill="var(--oval)"/>
    </svg>
    <p class="line serif finance-title">Financing Available</p>
    <p class="line body finance-line finance-line--1">We Finance everyone with approved credit</p>
    <p class="line body finance-line finance-line--2">Easy Payments: Monthly, Semi-Monthly or Weekly</p>
    <p class="line serif layaway">Ask about our Layaway plan</p>
    <p class="line serif hours-days">Open Mon-Sat</p>
    <p class="line serif hours-time">8:30 AM - 5 PM</p>
    <p class="line script social">Follow us on Friendlink : Brightway Auto Mart .inc</p>
    <p class="line website">BrightwayAutoMart.Com</p>
  </section>

</main>
</body>
</html>
```